Capability Statement Document/Flyer

Take the existing words from the capability statement document (attached) and design a unique folder/flyer document for professional use. Maybe something like a trifold or bifold style. Use approved colours and logo as per the attached files.
Our company designs and builds small onshore gas processing plants.

```html
<!DOCTYPE html>
<html lang="en">
<head>
<meta charset="utf-8">
<title>Tessaro Capability Statement</title>
<link href="https://fonts.googleapis.com/css2?family=Poppins:ital,wght@0,400;0,500;0,600;0,700;0,800;1,600&display=swap" rel="stylesheet">
<style>
:root{
  --green-dark:#075e4f;
  --green:#0f7a65;
  --green-light:#14876f;
  --grey:#e8e9eb;
  --board:#ececed;
  --bg:#dcdcde;
  --ink:#1d1d1d;
  --white:#ffffff;
}
*{box-sizing:border-box;margin:0;padding:0}
html,body{width:787px;height:1200px;overflow:hidden;background:var(--bg);font-family:'Poppins',sans-serif;color:var(--ink)}
.board{position:absolute;left:96px;top:15px;width:585px;height:1160px;background:var(--board);border-radius:40px;box-shadow:0 0 30px rgba(0,0,0,.08)}
.page{position:absolute;width:243px;height:342px;background:var(--white);overflow:hidden}
.p1{left:140px;top:60px}.p2{left:393px;top:60px}
.p3{left:140px;top:423px}.p4{left:393px;top:423px}
.p5{left:140px;top:786px}.p6{left:393px;top:786px}
.abs{position:absolute}
.photo{position:absolute}
.brand{position:absolute;font-weight:600;letter-spacing:.5px;line-height:1}

/* cover */
.p1{background:#1f4a42}
.cover-photo-top{left:0;top:0;width:243px;height:127px;background:linear-gradient(160deg,#3e5f58,#1f5349 60%,#2d6a5d)}
.cover-photo-bottom{left:0;top:232px;width:243px;height:110px;background:linear-gradient(180deg,#1f5a4d,#16443b)}
.cover-band{position:absolute;left:0;top:127px;width:243px;height:104px;background:var(--green);border-top:2px solid #fff;border-bottom:2px solid #fff}
.cover-title{position:absolute;left:17px;top:7px;color:#fff;font-weight:700;font-size:31.5px;line-height:36px;letter-spacing:.6px}
.cover-tag{position:absolute;left:16px;top:79px;color:#fff;font-size:7.4px;letter-spacing:.1px;white-space:nowrap}
.cover-url{position:absolute;left:86px;top:223px;width:70px;height:11px;border-radius:6px;background:var(--green);border:1px solid #fff;color:#fff;font-size:5px;font-weight:600;text-align:center;line-height:9.5px}
.p1 .brand{left:0;width:243px;top:24px;text-align:center;font-size:17px;color:#5fc2ab}

/* back cover */
.p2{background:var(--green-dark)}
.p2 .brand{left:0;width:243px;top:98px;text-align:center;font-size:21px;color:#fff}

/* page 3 */
.h-small{position:absolute;color:var(--green);font-weight:700;font-size:5px;letter-spacing:.1px}
.body-s{position:absolute;font-size:3.6px;line-height:4.6px;text-align:justify}
.p3-photo{left:13px;top:16px;width:216px;height:121px;border-radius:9px;background:linear-gradient(180deg,#b2c6de 0%,#c9d3dc 45%,#a7917a 70%,#8d8a80 100%)}
.principles{position:absolute;left:13px;top:189px;font-size:3.8px;line-height:8.1px;list-style:none}
.org-row{position:absolute;left:13px;width:124px;height:15px;background:var(--grey);border-radius:2px}
.org-label{position:absolute;left:0;width:46px;top:0;height:15px;display:flex;align-items:center;justify-content:center;text-align:center;color:var(--green);font-weight:600;font-size:3.8px;line-height:4.2px}
.org-box{position:absolute;top:2px;height:11px;width:19px;background:var(--green);border:.6px solid #fff;border-radius:1.5px;color:#fff;font-size:2.8px;display:flex;align-items:center;justify-content:center;text-align:center;line-height:3px}
.who{position:absolute;left:146px;top:172px;width:88px;height:170px;background:var(--green);border-radius:7px 7px 0 0;color:#fff;padding:6px 6px}
.who h3{font-size:6px;font-weight:700;margin-bottom:4px}
.who p{font-size:3.6px;line-height:4.9px;text-align:justify}
.who em{font-weight:600}

/* page 4 */
.h-mid{position:absolute;color:var(--green);font-weight:700;font-size:9.2px;letter-spacing:.1px}
.svc{position:absolute;left:14px;top:48px;width:214px;height:153px;background:var(--green-dark);border-radius:5px;overflow:hidden;color:#fff}
.svc-head{display:flex;height:12px;background:var(--green);align-items:center;font-size:4.6px;font-weight:600}
.svc-row{display:flex;align-items:center;font-size:3.5px;line-height:4px}
.c-num{flex:0 0 16px;width:16px;text-align:center}
.c-fn{flex:0 0 51px;width:51px;padding-left:5px;font-weight:600;color:#fff}
.c-sv{flex:1 1 auto;min-width:0;padding-left:3px;padding-right:4px}
.svc-body .c-num{color:#222;background:#fff;align-self:stretch;display:flex;align-items:center;justify-content:center}
.roles{position:absolute;left:14px;top:229px;width:182px;height:73px;border-radius:5px;overflow:hidden;background:var(--green-dark)}
.roles-head{display:flex;height:12px;background:var(--green);color:#fff;font-size:4.8px;font-weight:600;align-items:center}
.roles-body{display:flex;height:61px}
.roles-own{flex:0 0 68px;width:68px;background:var(--grey);font-size:3.6px;padding:6px 6px;line-height:10.4px}
.roles-pdp{flex:1;color:#fff;font-size:3.6px;padding:6px 10px;line-height:10.4px}

/* page 5 */
.panel{position:absolute;top:9px;width:112px;height:120px;background:var(--green);border-radius:4px;color:#fff;padding:6px 6px}
.panel h2{font-size:13px;font-weight:600;line-height:16px}
.panel ul{list-style:none;font-size:3.9px;line-height:5px}
.panel li{margin-bottom:4px;padding-left:4px;position:relative}
.panel li::before{content:"•";position:absolute;left:0}
.icon{position:absolute}
.p5-photo{left:8px;top:133px;width:227px;height:192px;border-radius:8px;background:linear-gradient(180deg,#8fa7c4 0%,#b8c6d6 50%,#cfd3d6 72%,#a59888 88%,#8a7d6e 100%)}
.p5 .brand{left:8px;width:227px;top:208px;text-align:center;font-size:30px;color:var(--green)}
.contact{position:absolute;right:0;top:325px;width:110px;height:17px;background:var(--green);color:#fff;font-size:3.9px;font-weight:600;text-align:right;padding:2px 16px 0 0;line-height:4.8px}

/* page 6 */
.p6-title{position:absolute;left:0;width:243px;top:20px;text-align:center;color:#fff;font-weight:700;font-size:12.4px}
.person{position:absolute;left:13px;width:217px}
.bar{display:flex;height:10px;border-radius:5px;overflow:hidden;color:#fff;font-size:5px;font-weight:600;align-items:center;background:var(--green-dark)}
.bar span{display:flex;align-items:center;height:100%;padding-left:4px;white-space:nowrap}
.b-lab{flex:0 0 35px;justify-content:center;background:var(--green);padding-left:0!important}
.b-name{flex:0 0 66px;border-right:.6px solid #fff}
.b-role{flex:0 0 33px;justify-content:center;padding-left:0!important;border-right:.6px solid #fff}
.b-val{flex:1}
.exp{display:flex;font-size:3.9px;margin-top:4px;font-weight:600}
.exp b{color:var(--green);flex:0 0 35px;padding-left:5px;font-weight:600}
.exp span{flex:1;min-width:0}
.bio{font-size:3.6px;line-height:5.2px;margin-top:4px;padding-left:3px;text-align:justify}
</style>
</head>
<body>
<div class="board"></div>

<section class="page p1">
  <div class="photo cover-photo-top" role="img" aria-label="Gas processing plant with solar arrays, toned green"></div>
  <div class="photo cover-photo-bottom" role="img" aria-label="Plant pipework and valves, toned green"></div>
  <div class="brand">TESSARO</div>
  <div class="cover-band">
    <h1 class="cover-title">CAPABILITY<br>STATEMENT</h1>
    <p class="cover-tag">SIMPLIFY PROJECT EXECUTION, STREAMLINE OPERATIONS</p>
  </div>
  <div class="cover-url">www.tessaro.com.au</div>
</section>

<section class="page p2">
  <div class="brand">TESSARO</div>
</section>

<section class="page p3">
  <svg class="abs" style="left:0;top:0" width="243" height="30" viewBox="0 0 243 30"><path d="M0 0H243L243 3Q120 8 0 25Z" fill="var(--green)"/></svg>
  <div class="photo p3-photo" role="img" aria-label="Onshore gas processing facility with pipework"></div>
  <h3 class="h-small" style="left:13px;top:145px">WHAT IS A PROJECT DELIVERY PARTNER?</h3>
  <p class="body-s" style="left:13px;top:155px;width:216px">A Project Delivery Partner (PDP) provides integrated project management along with technical, commercial and delivery support services to help an organisation successfully deliver a project. The PDP acts as the owner's team while the owner retains accountability and key decision-making authority.</p>
  <h3 class="h-small" style="left:13px;top:180px">PDP CORE PRINCIPLES:</h3>
  <ol class="principles">
    <li>&nbsp;1.&nbsp;&nbsp;Owner controls the project</li>
    <li>&nbsp;2.&nbsp;&nbsp;PDP enables delivery &amp; provides assurance</li>
    <li>&nbsp;3.&nbsp;&nbsp;Contractors execute the work</li>
  </ol>
  <h3 class="h-small" style="left:13px;top:225px">PDP OBJECTIVE:</h3>
  <p class="body-s" style="left:13px;top:236px;width:124px;font-size:3.8px;line-height:5.4px">Deliver the project safely, on schedule, within budget and ready for operations; providing owner capability throughout the project lifecycle.</p>
  <svg class="abs" style="left:13px;top:265px" width="124" height="55"><path d="M78 15V20M78 35V40M53 40H103M53 37V40M103 37V40" stroke="#bbb" stroke-width=".4" fill="none"/></svg>
  <div class="org-row" style="top:265px"><div class="org-label">Owner</div><div class="org-box" style="left:69px">Operator XYZ</div></div>
  <div class="org-row" style="top:285px"><div class="org-label">Project Delivery Partner</div><div class="org-box" style="left:69px">Tessaro</div></div>
  <div class="org-row" style="top:305px"><div class="org-label">Contractors</div><div class="org-box" style="left:43px">Engineering</div><div class="org-box" style="left:69px">Suppliers</div><div class="org-box" style="left:95px">Execution</div></div>
  <div class="who">
    <h3>WHO ARE TESSARO?</h3>
    <p><b>Tessaro</b> are a highly experienced team of Executive, Project, Construction, Commissioning and Operations specialists who combine deep technical knowledge with proven leadership to deliver unique <b>Project Delivery Partner</b> services to organisations in Australia.</p>
    <p style="margin-top:7px"><em><i>Our vision is straightforward:</i></em></p>
    <p style="margin-top:3px;color:#dff"><em><i>Simplify Project Execution, Streamline Operations.</i></em></p>
  </div>
  <svg class="abs" style="left:0;top:310px" width="243" height="32" viewBox="0 0 243 32"><path d="M0 32V30Q150 30 220 10Q240 5 243 20V32Z" fill="var(--grey)"/></svg>
</section>

<section class="page p4">
  <svg class="abs" style="left:0;top:0" width="243" height="24" viewBox="0 0 243 24"><path d="M0 0H243V8Q240 24 222 22L40 4Q20 2 0 0Z" fill="var(--green)"/></svg>
  <h2 class="h-mid" style="left:20px;top:30px">PDP SERVICES:</h2>
  <div class="svc">
    <div class="svc-head"><span class="c-num">#</span><span class="c-fn">FUNCTION</span><span class="c-sv">TESSARO SERVICE</span></div>
    <div class="svc-body">
      <div class="svc-row" style="height:11px"><span class="c-num">1</span><span class="c-fn">Project Management</span><span class="c-sv">Planning, Reporting &amp; Delivery Leadership from Concept to Completion</span></div>
      <div class="svc-row" style="height:13px"><span class="c-num">2</span><span class="c-fn">Engineering</span><span class="c-sv">Concept Selection, Design Coordination, Technical Assurance &amp; Value Engineering</span></div>
      <div class="svc-row" style="height:13px"><span class="c-num">3</span><span class="c-fn">Procurement</span><span class="c-sv">Contracting Strategy, Tender Process &amp; Supplier / Contractor Management</span></div>
      <div class="svc-row" style="height:10px"><span class="c-num">4</span><span class="c-fn">Approvals</span><span class="c-sv">Land Access, Regulator Engagement, Safety Case, Permits &amp; Licenses</span></div>
      <div class="svc-row" style="height:10px"><span class="c-num">5</span><span class="c-fn">Cost Control</span><span class="c-sv">Budget Development, Forecasting &amp; Management</span></div>
      <div class="svc-row" style="height:12px"><span class="c-num">6</span><span class="c-fn">Scheduling</span><span class="c-sv">Master Schedule Development, WBS, Resource Allocation, Monitoring &amp; Updating</span></div>
      <div class="svc-row" style="height:10px"><span class="c-num">7</span><span class="c-fn">Risk Management</span><span class="c-sv">Risk Register, Identification, Mitigation &amp; Reporting</span></div>
      <div class="svc-row" style="height:10px"><span class="c-num">8</span><span class="c-fn">Governance</span><span class="c-sv">Risk Register, Identification, Mitigation &amp; Reporting</span></div>
      <div class="svc-row" style="height:10px"><span class="c-num">9</span><span class="c-fn">Construction</span><span class="c-sv">Management &amp; Coordination of Contractor Execution Teams</span></div>
      <div class="svc-row" style="height:13px"><span class="c-num">10</span><span class="c-fn">Commissioning &amp; Start-up</span><span class="c-sv">Lead Commissioning &amp; Start-up, Completions System, Bring the Facility to Steady-State</span></div>
      <div class="svc-row" style="height:10px"><span class="c-num">11</span><span class="c-fn">Operations Readiness</span><span class="c-sv">People &amp; Organisation, Process &amp; Procedures, Systems &amp; Technology</span></div>
      <div class="svc-row" style="height:14px"><span class="c-num">12</span><span class="c-fn">Operations &amp; Maintenance</span><span class="c-sv">Monitor &amp; Operate Asset, Minimize Downtime, Lowest Possible OPEX for Owner</span></div>
    </div>
  </div>
  <h2 class="h-mid" style="left:20px;top:213px">PDP ROLES &amp; RESPONSIBILITIES:</h2>
  <div class="roles">
    <div class="roles-head"><span style="flex:0 0 68px;padding-left:7px">OWNER</span><span style="padding-left:10px">TESSARO SERVICE</span></div>
    <div class="roles-body">
      <div class="roles-own">Sets Project Objectives<br>Approves Major Decisions<br>Holds Project Risk<br>Awards Contracts<br>Provides Funding</div>
      <div class="roles-pdp">Develops Delivery Plans<br>Provides Recommendations<br>Identifies and Manages Risks<br>Manages Contractor Interfaces<br>Monitors Cost and Schedule Performance</div>
    </div>
  </div>
  <svg class="abs" style="left:0;top:310px" width="243" height="32" viewBox="0 0 243 32"><path d="M0 32V25Q5 5 30 4Q140 8 243 32Z" fill="var(--green)"/></svg>
</section>

<section class="page p5">
  <svg class="abs" style="left:0;top:0" width="243" height="26" viewBox="0 0 243 26"><path d="M0 0H243Q245 20 225 25L150 17Z" fill="var(--grey)"/></svg>
  <div class="panel" style="left:8px">
    <h2>PDP<br>BENEFITS:</h2>
    <svg class="icon" style="left:45px;top:6px" width="22" height="20" viewBox="0 0 22 20" fill="none" stroke="#fff" stroke-width="1"><circle cx="12" cy="6" r="4"/><path d="M10 9L9 13L12 11L15 13L14 9"/><path d="M2 15Q7 13 11 15H16Q20 13 21 12"/></svg>
    <ul style="margin-top:9px">
      <li>Provides owners with access to experienced project delivery capability</li>
      <li>Improved project controls and governance</li>
      <li>Greater flexibility than traditional EPC delivery</li>
      <li>Enhanced visibility and management of cost, schedule and risk</li>
      <li>Scalable resources aligned with project phases</li>
    </ul>
  </div>
  <div class="panel" style="left:123px">
    <h2 style="margin-top:10px">PDP<br>CHALLENGES:</h2>
    <svg class="icon" style="left:38px;top:16px" width="18" height="16" viewBox="0 0 18 16" fill="none" stroke="#fff" stroke-width="1"><circle cx="12" cy="5" r="3.5"/><path d="M1 15H17M3 15V9M3 9L8 11M6 15V12"/></svg>
    <ul style="margin-top:9px">
      <li>Owner retains significant delivery risk</li>
      <li>Requires clear governance and decision making processes</li>
      <li>Multiple contractor interfaces require strong coordination</li>
      <li>Success depends on collaborative Owner-PDP relationship</li>
    </ul>
  </div>
  <div class="photo p5-photo" role="img" aria-label="Gas plant under blue sky framed by solar panels"></div>
  <div class="brand">TESSARO</div>
  <svg class="abs" style="left:0;top:318px" width="243" height="24" viewBox="0 0 243 24"><path d="M0 24V16Q60 20 130 7H243V24Z" fill="var(--green)"/></svg>
  <div class="contact">FOR MORE INFORMATION CONTACT:<br>DIRECTORS@TESSARO.COM.AU</div>
</section>

<section class="page p6">
  <svg class="abs" style="left:0;top:0" width="243" height="70" viewBox="0 0 243 70">
    <defs><linearGradient id="hdr" x1="0" x2="1"><stop offset="0" stop-color="#14876f"/><stop offset="1" stop-color="#075e4f"/></linearGradient></defs>
    <path d="M0 0H243V20Q243 62 200 68Q120 55 0 48Z" fill="url(#hdr)"/>
  </svg>
  <h2 class="p6-title">KEY TESSARO PERSONNEL</h2>

  <div class="person" style="top:84px">
    <div class="bar"><span class="b-lab">NAME:</span><span class="b-name">MARK DALTON</span><span class="b-role">ROLE:</span><span class="b-val">EXECUTIVE DIRECTOR</span></div>
    <div class="exp"><b>35yrs Exp:</b><span>Crestline Energy, Northsea Petro, GRX Partners, Arcfield Energy</span></div>
    <p class="bio">Extensive global energy industry experience, from frontline O&amp;M to the boardroom. Respected 'C Suite' leader with a track record of building high performing teams that deliver outstanding results.</p>
  </div>

  <div class="person" style="top:136px">
    <div class="bar"><span class="b-lab">NAME:</span><span class="b-name">NEIL HARCOURT</span><span class="b-role">ROLE:</span><span class="b-val">TECHNICAL DIRECTOR</span></div>
    <div class="exp"><b>40yrs Exp:</b><span>Westgate Energy, Kairo Gas, Halden Oil, GRX Partners, Arcfield Energy</span></div>
    <p class="bio">Senior Logistics &amp; Supply Chain Manager / Procurement Manager with strong operational, commercial, project management, negotiating &amp; relationship building skills. Experienced in operating complex and diverse logistics operations, significantly improving service levels whilst reducing cost.</p>
  </div>

  <div class="person" style="top:195px">
    <div class="bar"><span class="b-lab">NAME:</span><span class="b-name">PETER LINDQVIST</span><span class="b-role">ROLE:</span><span class="b-val">COMMERCIAL DIRECTOR</span></div>
    <div class="exp"><b>39yrs Exp:</b><span>Crestline Energy, Northsea Petro, Gulf Basin Petroleum, Halden Oil, Brightwater Group, Coastal Gas Co, GRX Partners, Arcfield Energy</span></div>
    <p class="bio">Highly skilled &amp; experienced operations &amp; project management professional with 39 years' experience in the global oil &amp; gas industry delivering multiple projects and establishing best in class operational assets. Deep knowledge of project management, construction, commissioning &amp; start-up including a global functional assurance role.</p>
  </div>

  <div class="person" style="top:263px">
    <div class="bar"><span class="b-lab">NAME:</span><span class="b-name">SAM WHITFORD</span><span class="b-role">ROLE:</span><span class="b-val">OPERATIONS DIRECTOR</span></div>
    <div class="exp"><b>27yrs Exp:</b><span>Halden Oil, Brightwater Group, Coastal Gas Co, GRX Partners, Arcfield Energy</span></div>
    <p class="bio">27 years' success leading operations, maintenance and commissioning teams on on shore and offshore oil and gas production platforms, FPSOs, gas processing, coal seam gas, refrigeration facilities, and chemical refineries.</p>
    <p class="bio" style="margin-top:5px">Results driven and enthusiastic Leader with a proven track record of delivery.</p>
  </div>
</section>
</body>
</html>
```